Vallée douce coffee - Label design

Watchout: Keep in mind while you submit it needs to be a LABEL (that will be sticked on brown kraft 250 g side gusset coffee pouches). No custom pack for time being (need more scale to custom print pack).

Looking for a label design for my new Beau Matin collection of freshly roasted, single origin specialty coffee. Brand name is Vallée Douce (it means red earth and alludes to the soil coffee grows on at high altitude in Africa. It also alludes to the red color of the coffee fruit). Brand selling line is "Pure Origin Coffee". Label to go as stickers on 250 g side gusset coffee pouches in Kraft brown paper (will print labels and stick on packs, packs are 80 mm wide and 260 mm long). This is a relatively complex project comprising the "vallée douce" brand logo (funded separately, winner will have the job), the "Beau Matin" collection visual identity, iconic assets for brand and collection recognition across lineup, educational visual icons, text placeholders. It needs to combine hard point visual elements and soft points (text placeholder) which I can easily edit on need basis (text needs to be "outlines" for easy editing after submission). Winner of label submission gets to design brand logo. I will ultimately need 3 different labels for our Beau Matin collection, one for each continent our coffee comes from (Africa, Asia, Latin America). This pitch should focus on the Africa one only. Winner will then have opportunity to design the other ones in consistent way.

BRIEF:
We roast single origin, high quality specialty coffee from high altitude estates in Africa (volcanic slopes in Congo and Burundi, Highlands in Ethiopia and Kenya) Design need to induce the premiumness of the proposition (this is a collection called "Beau Matin"), as well the the unique geographical origins of our coffee (without being too specific as we want to use same label for all our African origins) -oversized shape of continent in background + some visuals conveying the African roots could work well. It needs to create a mental Journey "back to the origins" - of mankind, of unique terroirs creating the best coffee, of our unspoilt roots. So the Journey themes is critical (to be expressed by the telegram type of font, by the way Africa is brought to life,etc.). At the same time keep in mind label space is limited (label stickers go on 250 g coffee pouches made in kraft brown paper) and we want to have a pure design, which leaves room to the text placeholder (see below) and is easily recognizable and reapplicable across the SKUs (we will add Asia and Latin America packs once we lock Africa). As such we need to strike right balance between visual differentiation by origin (Africa, Asia, Latin America) and common iconic assets for brand recognition and lineup harmonization (same font, same way the continent is brought to life, same structure of the label, differentiation by color background,etc.).

We need placeholder for text that will specify exact name of estate, county of origin, coffee type, roasting level and tasting notes. Here I will allow myself some creative direction: it should be in the format of a vintage luggage tag (see attached examples) where we can edit content in Telegram font (our coffee sourcing changes often). We will need to assess if the tag remains standard across collection, or whether we are able to give it a visual twist for each origin (Africa, Asia, Latin America). That would be nicer (see Moonpeak "Ledgers" example), but priority of the text placeholder is clarity of information above anything else.

Last nice to have (if it time allows) we need educational visual icons (ideally as separate small round labels we can stick on the pack above the main label) for recommended brewing method (filter, espresso, italian moka, french press).

Reason: Still looking for the design in line with brief. Will send feedback to the top 3 routes today.

Target Market(s)

Switzerland

Industry/Entity Type

Coffee Shop

Logo Text

Vallée douce -Pure Origin Coffee

Font styles to use
Other font styles liked:
• TELEGRAM type of font to induce geographical journey, single origin,.. For the "luggage tag" placeholder

Requirements
Must have
• - Brand name: Vallée Douce. Brand selling line: Pure Origin Coffee. Brand Logo: winner of label submission gets to design brand logo
• - Collection name: BEAU MATIN (written, I can see well as a vertical block). name of SKU: AFRICA (visualized a must, written tbc).
• - Text place holder (vintage luggage tag in telegram font) : we will show there name of estate, country of origin, tasting notes. I could see nicely a baggage tag format, where we fill in the details in telegram type of font.
• - 100% single origin Arabica (at the bottom)
• - 250 g (at the bottom)
• Technical Specs:
• A. Artwork must be supplied in either Adobe illustrator or Adobe Photoshop files or Coral Draw files
• B. Create all text in artwork in ‘ outlines ’
• C. The resolution of photographic image files must be no less than 350 dpi
• D. Never flatten the file as we require all layers
• E. All Photoshop image files should be linked and attached. Never flatten the layers and do not change the directory
• F. Create the images with CMYK colour mode ( RGB colour mode is not for printing)
• G. If you are going to use a spot colour please reference the Pantone ( PMS #)
• H. Designate all ‘Transparent’ areas in the artwork with a custom Pantone colour as well as designating the layer’s name as ‘ Transparent’. Please indicate specifically which pantone colour is designated for the ‘transparent’ area.
• I. Reduce any barcodes to 85% as a minimum scale
Nice to have
• - educational simple visual icons on recommended brewing method (filer, italian moka, french press or espresso) as additional small stickers to stick above main label

```html
<!DOCTYPE html>
<html lang="en">
<head>
<meta charset="utf-8">
<title>Vallée Douce – Beau Matin Africa Label</title>
<link rel="stylesheet" href="https://fonts.googleapis.com/css2?family=Oswald:wght@300;400;500&family=Quicksand:wght@300;700&family=Roboto+Condensed:wght@400;700&display=swap">
<style>
  :root {
    --backdrop: #d9dadf;
    --roast-brown: #5e3a08;
    --bean-brown: #7a4b22;
    --kraft-tan: #b58a5a;
    --earth-red: #cc4130;
    --ink-brown: #6b3c14;
    --paper-white: #ffffff;
  }
  html, body {
    margin: 0;
    padding: 0;
    width: 1200px;
    height: 1200px;
    overflow: hidden;
    background: var(--backdrop);
  }
  .artboard {
    position: relative;
    width: 1200px;
    height: 1200px;
  }
  .brew-sticker {
    position: absolute;
    left: 519px;
    top: 70px;
    width: 162px;
    height: 162px;
  }
  .main-label {
    position: absolute;
    left: 429px;
    top: 269px;
    width: 342px;
    height: 856px;
  }
  .brand-name { font-family: "Oswald", sans-serif; font-weight: 400; }
  .tagline { font-family: "Oswald", sans-serif; font-weight: 500; }
  .collection-name { font-family: "Quicksand", sans-serif; }
  .origin-name { font-family: "Oswald", sans-serif; font-weight: 300; }
  .tag-field { font-family: "Roboto Condensed", sans-serif; font-weight: 700; }
  .claim { font-family: "Roboto Condensed", sans-serif; }
  .net-weight { font-family: "Roboto Condensed", sans-serif; }
  .brew-method { font-family: "Oswald", sans-serif; }
</style>
</head>
<body>
<main class="artboard">

  <!-- Brewing method round sticker -->
  <svg class="brew-sticker" viewBox="0 0 112 112" aria-label="Brewing method sticker: French press">
    <defs>
      <radialGradient id="icon-glow" cx="50%" cy="50%" r="50%">
        <stop offset="0%" stop-color="#ffffff" stop-opacity="0.55"/>
        <stop offset="100%" stop-color="#ffffff" stop-opacity="0"/>
      </radialGradient>
    </defs>
    <circle cx="56" cy="56" r="55" fill="var(--earth-red)"/>
    <circle cx="56" cy="56" r="47" fill="var(--paper-white)"/>
    <clipPath id="sticker-inner"><circle cx="56" cy="56" r="44"/></clipPath>
    <g clip-path="url(#sticker-inner)">
      <rect x="0" y="0" width="112" height="112" fill="var(--roast-brown)"/>
      <rect x="0" y="74" width="112" height="40" fill="var(--paper-white)"/>
      <rect x="0" y="66" width="112" height="8" fill="var(--kraft-tan)"/>
    </g>
    <ellipse class="brew-icon" cx="56" cy="42" rx="18" ry="20" fill="url(#icon-glow)" role="img" aria-label="French press icon"/>
    <text class="brew-method" x="56" y="86" text-anchor="middle" font-size="8.5" fill="var(--roast-brown)"><tspan font-weight="400">FRENCH</tspan><tspan font-weight="500">PRESS</tspan></text>
  </svg>

  <!-- Main label -->
  <svg class="main-label" viewBox="0 0 236 590" aria-label="Vallée Douce Beau Matin Africa label">
    <defs>
      <radialGradient id="ornament-soft" cx="50%" cy="50%" r="50%">
        <stop offset="0%" stop-color="#b58a5a" stop-opacity="0.75"/>
        <stop offset="100%" stop-color="#b58a5a" stop-opacity="0"/>
      </radialGradient>
      <radialGradient id="map-soft" cx="50%" cy="45%" r="55%">
        <stop offset="0%" stop-color="#b58a5a"/>
        <stop offset="100%" stop-color="#e6d3bd"/>
      </radialGradient>
    </defs>

    <!-- Brown field -->
    <rect class="label-field" x="0" y="0" width="236" height="402" fill="var(--roast-brown)"/>

    <!-- Corner accents -->
    <circle cx="12" cy="10" r="7" fill="url(#ornament-soft)" role="img" aria-label="Corner ornament"/>
    <circle cx="224" cy="10" r="7" fill="url(#ornament-soft)" role="img" aria-label="Corner ornament"/>
    <circle cx="12" cy="390" r="7" fill="url(#ornament-soft)" role="img" aria-label="Corner ornament"/>
    <circle cx="224" cy="390" r="7" fill="url(#ornament-soft)" role="img" aria-label="Corner ornament"/>

    <!-- White arched panel -->
    <path class="arch-rim" d="M0 84 Q118 34 236 84" fill="none" stroke="var(--kraft-tan)" stroke-width="5"/>
    <path class="arch-panel" d="M0 90 Q118 40 236 90 L236 290 Q118 325 0 290 Z" fill="var(--paper-white)"/>
    <path class="arch-base-band" d="M0 290 Q118 325 236 290 L236 300 Q118 335 0 300 Z" fill="var(--earth-red)"/>

    <!-- Brand -->
    <circle class="brand-dot" cx="118" cy="42" r="16" fill="var(--earth-red)" stroke="var(--paper-white)" stroke-width="3"/>
    <text class="brand-name" x="118" y="104" text-anchor="middle" font-size="21" fill="var(--ink-brown)">VALLÉE DOUCE</text>
    <text class="tagline" x="118" y="120" text-anchor="middle" font-size="8" letter-spacing="1" fill="var(--ink-brown)">- PURE ORIGIN COFFEE -</text>

    <!-- Collection -->
    <ellipse cx="118" cy="149" rx="14" ry="12" fill="url(#ornament-soft)" role="img" aria-label="Decorative flourish"/>
    <ellipse cx="118" cy="198" rx="107" ry="33" fill="var(--kraft-tan)"/>
    <ellipse cx="118" cy="198" rx="102" ry="29" fill="var(--bean-brown)"/>
    <ellipse cx="118" cy="198" rx="98" ry="26" fill="none" stroke="var(--kraft-tan)" stroke-width="0.8"/>
    <text class="collection-name" x="118" y="207" text-anchor="middle" font-size="25" fill="var(--paper-white)"><tspan font-weight="300">Beau</tspan><tspan font-weight="700">Matin</tspan></text>
    <ellipse cx="118" cy="252" rx="20" ry="18" fill="url(#ornament-soft)" role="img" aria-label="Decorative flourish"/>

    <!-- Origin -->
    <circle cx="118" cy="318" r="32" fill="var(--paper-white)" stroke="var(--roast-brown)" stroke-width="2.5"/>
    <circle cx="118" cy="318" r="25" fill="url(#map-soft)" role="img" aria-label="Map of the African continent"/>
    <text class="origin-name" x="118" y="377" text-anchor="middle" font-size="22" letter-spacing="4" fill="var(--paper-white)">AFRICA</text>

    <!-- Red info band -->
    <rect class="info-band" x="0" y="402" width="236" height="188" fill="var(--earth-red)"/>

    <!-- Luggage tag table -->
    <g class="luggage-tag" fill="var(--paper-white)" stroke="var(--ink-brown)" stroke-width="0.6">
      <rect x="14" y="415" width="206" height="82"/>
      <line x1="14" y1="442" x2="220" y2="442"/>
      <line x1="14" y1="470" x2="220" y2="470"/>
      <line x1="119" y1="442" x2="119" y2="497"/>
    </g>
    <g class="tag-field" font-size="4.5" fill="var(--ink-brown)">
      <text x="17" y="421">DESTINATION</text>
      <text x="17" y="448">WEIGHT</text>
      <text x="122" y="448">COUNTRY</text>
      <text x="17" y="476">HEIGHT</text>
      <text x="122" y="476">Nº</text>
    </g>

    <!-- Claims -->
    <text class="claim" x="14" y="523" font-size="14" fill="var(--paper-white)"><tspan font-weight="700">100%</tspan> SINGLE ORIGIN ARABICA</text>
    <text class="net-weight" x="220" y="560" text-anchor="end" font-size="22" fill="var(--paper-white)"><tspan font-weight="700">250</tspan><tspan font-weight="400">gr.</tspan></text>
  </svg>

</main>
</body>
</html>
```